Coaching landingpage/salespage need a layout

Hi!
We are two people from Sweden looking for help to design our coaching landingpage/salespage.

What about:
We need a nice modern timeless appealing Photoshop layout (landingpage) for our coaching page where we coach people to “how to get a richer lifestyle”.

Style of page:
We want the site to reflect seriousness but still harmonic. We would like somewhat colorful and (but not too crazy). After all, we are coaching about investments and private economy.
Responsive layout – consider stacking order when scaling down window width. Fullpage-design where content areas are 960 grid/max-width.

----------------------------------------------------------------------------
Content on page:
*Headersection – Logo and header image with the two coaches together and space for later on adding a video.

*On the landingpage the customers can read up on what we mean by a richer lifestyle (use dummy text). We show our Trivselsnyckeln (= Lifestyle matrix) and a little description about that. If the customers want to know more, they can click "read more (or a symbolic icon that relates to read more)" to expand a hidden div (section) where they can read more about Trivselsnyckeln. They can also minimize the section.

*3-4 Unique selling points “Four reasons why choose coaching” with nice designed number-icons and some place for text.

*The customer should also be able to read something about what happens during a typical coaching session, some bullets that summarize it (use dummy text) and a couple of headlines, maybe 3 or 4 (about what they need to prepare for themselves .eg Skype, headset/microphone etc).

*Offer/product section: A section where the customer can see what services we provide, choose product and click order. When customer click order they will arrive to an order-page (this one you don’t have to design) .
Our products are as followed: Bronze (single coaching session), Silver (small-package), Gold (large-package). Use provided graphics for these products.

*Testimonials section. Currently we have 2 good testimonials, but only with text no portrait picture.

Testimonial1: “Uppiggande och inspirerande! Kommer med enkla vardagstips såväl som svårare tips. Ett roligt sätt att få en spark i baken, så att ekonomi-energin bibehålls! Tack för ett bra samtal!" - Josefin Brandeby

Testimonial2: "Värdefullast för mig var kunskapen om alternativa investeringssställen som inte är börs eller eget ägande." - Annika Sjöhalla

*Section with portraits and info about the coaches (currently 2 coaches, but in future will be several, so a design-section that’s lets us add more coaches).

*Footer-section
------------------------------------------------------------------------

Colors:
Use Trivselsnyckeln (attached file) as colorinspiration. Doesn’t have to be exactly those colors, you can use similar colors if it is more pleasing to the eye and you can also use complementary colors.

Currently we have tried of our own but don't really nail it with any apealing design. This is what we have done so far but we want to replace it with your more professional design:

https://www.harbekrona.se/full/Page/coaching13
-------------------------------------------------------------

SUMMARIZE of the above design-description:

* Our logo (attached psd-file with smart-object. You can try different colors with color-overlay)

*Apealing headerimage with portrait (attached file "big_portrait")

*Introduction text (use dummy text about 100 words)

*Text about Trivselsnyckeln (use dummy text about 200 words)

*Trivselsnyckeln (attached psd-file with smart-object)

*What we are covering during a coaching session (dummy text about 200 words and about 5 or 6 bullets)

*3-4 Unique Selling Points with stylish number icons (not 2 small) and some text.
*Our offers Bronze, Silver, Gold (attached pictures)
*Testimonials
*Picture & info about coaches (attached pictures, choose whichever suits you)
*Footer

Please comment if there are questions.

Reagards Torbjörn @ Harbe Krona

Target Market(s)

People who want to learn how to create a richer lifestyle which involves more freedom and a better well-being

Number of Pages Required

1 page

Font styles to use
Sans Serif
Other font styles liked:
• Roboto

Requirements
Should not have
• A cheezy unmodern landingpage with lots of texts and 10 sign-up buttons.
• This page is not a site about capturing emails and building lists by provide a "best-guide-for-something". It´s about getting people to book and pay for one or more coaching-sessions.

```html
<!DOCTYPE html>
<html lang="sv">
<head>
<meta charset="utf-8">
<title>Harbe Krona – Livsstilscoaching</title>
<link rel="stylesheet" href="https://fonts.googleapis.com/css2?family=Noto+Sans:wght@400;500;700&display=swap">
<style>
:root{
  --navy:#0b0c24;
  --navy-band:#1b1a42;
  --hero-deep:#0f2c6e;
  --hero-light:#3f7fd0;
  --red:#e60000;
  --red-band:#d10000;
  --lavender:#eeeef8;
  --panel:#f1f1fa;
  --ink:#1e1e28;
  --muted:#555560;
  --orange:#ef5a1c;
  --footer:#2b2b2b;
  --white:#ffffff;
}
*{box-sizing:border-box;margin:0;padding:0}
html,body{width:1200px;height:2915px;overflow:hidden}
body{font-family:"Noto Sans",Arial,sans-serif;color:var(--ink);background:var(--white);position:relative;font-size:16px;line-height:1.45}
.abs{position:absolute}

/* top bar */
.topbar{left:0;top:0;width:1200px;height:74px;background:var(--navy);border-bottom:4px solid #cfd3dc}
.brand{left:195px;top:16px;display:flex;align-items:center;gap:12px;color:#c9d3e6}
.brand-mark{width:40px;height:28px;background:#9fb2d3}
.brand-name{font-size:25px;letter-spacing:2px;line-height:1;font-weight:400}
.brand-sub{font-size:13px;letter-spacing:1px;color:var(--white);margin-top:3px}

/* hero */
.hero{left:0;top:78px;width:1200px;height:453px;background:radial-gradient(ellipse at 52% 60%,var(--hero-light) 0%,#1f55a8 35%,var(--hero-deep) 75%,#081a45 100%)}
.hero-people{left:370px;top:205px;width:430px;height:277px;background:linear-gradient(180deg,#8a9ab5 0%,#3a3f4f 70%,#24262e 100%);border-radius:120px 120px 0 0;opacity:.85}
.hero-tagline{left:244px;top:107px;width:702px;height:53px;background:rgba(200,200,210,.85);font-size:17px;display:flex;align-items:center;justify-content:center;color:#111}

/* welcome */
.welcome{left:185px;top:482px;width:824px;height:275px;background:#f5f5fb;box-shadow:0 2px 8px rgba(0,0,0,.25);padding:30px 26px 0 30px}
.welcome h1{font-size:22px;font-weight:400;display:flex;align-items:center;gap:12px;margin-bottom:6px}
.dot{width:18px;height:18px;border-radius:50%;background:var(--red);box-shadow:inset -3px -3px 0 #a00}
.welcome p{font-size:16px;line-height:1.35;margin-bottom:20px}
.read-more{color:#888;font-style:italic;font-size:13px;margin-left:10px}
.chev{display:inline-block;vertical-align:middle}

/* reasons */
.reasons{left:0;top:776px;width:1200px;height:219px;background:var(--navy-band)}
.section-title{display:flex;align-items:center;gap:12px;font-size:18px;font-weight:500;letter-spacing:.5px}
.reasons .section-title{position:absolute;left:185px;top:10px;color:var(--white)}
.reason{position:absolute;top:49px;width:168px;height:141px;background:var(--red);color:var(--white);padding:16px 10px 0 74px;font-size:10.5px;line-height:1.25}
.reason strong{display:block;font-size:11px;margin-bottom:10px}
.reason svg{position:absolute;left:10px;top:14px}
.reason .curl{position:absolute;right:0;bottom:0;width:32px;height:32px;background:linear-gradient(135deg,var(--red) 50%,#e9e9e9 50%,#bbb 100%)}

/* sessions */
.sessions{left:0;top:995px;width:1200px;height:566px;background:var(--lavender)}
.sessions .section-title{position:absolute;left:185px;top:20px;color:var(--ink)}
.sessions .body{position:absolute;left:218px;top:58px;width:772px;font-size:16px;line-height:1.35}
.bullets{list-style:none;margin:22px 0 14px -2px}
.bullets li{display:flex;align-items:center;gap:12px;margin-bottom:17px}
.bullets .dot{width:14px;height:14px;box-shadow:inset -2px -2px 0 #a00}
.sessions h3{font-size:16.5px;font-weight:500;margin:0 0 18px}
.sessions .para{margin-bottom:24px}

/* services */
.services{left:0;top:1561px;width:1200px;height:546px;background:var(--white)}
.services .section-title{position:absolute;left:185px;top:25px}
.plans{position:absolute;left:185px;top:78px;width:824px;height:410px;background:var(--panel);display:flex}
.plan{flex:1;text-align:center;padding-top:44px;position:relative}
.plan+.plan{border-left:1px solid #d3d3e0}
.plan:not(:first-child)::before{content:none}
.medal{width:166px;height:166px;border-radius:50%;margin:0 auto 40px;box-shadow:0 12px 14px -8px rgba(0,0,0,.35)}
.bronze{background:radial-gradient(circle at 40% 35%,#f3b36c,#d57a2a 60%,#a6551a)}
.silver{background:radial-gradient(circle at 40% 35%,#f2f2f2,#c5c5c5 60%,#939393)}
.gold{background:radial-gradient(circle at 40% 35%,#fff07a,#f2c51d 60%,#c99708)}
.plan h4{font-size:17px;font-weight:400;line-height:1.1}
.plan .kind{font-size:13px}
.plan .note{font-size:12.5px;color:var(--muted);margin-top:14px}
.order{position:absolute;left:50%;transform:translateX(-50%);bottom:12px;display:flex;align-items:center;width:170px;height:40px;background:var(--ink);border-radius:20px;color:var(--white);font-size:14px}
.order .circle{width:44px;height:44px;border-radius:50%;background:var(--red);border:3px solid var(--white);margin-left:-4px;margin-right:12px}
.guarantee{position:absolute;left:0;width:1200px;top:497px;text-align:center;font-size:12.5px;color:#1c3b6b}

/* testimonials */
.testimonials{left:0;top:2107px;width:1200px;height:133px;background:var(--red-band);color:var(--white)}
.tab{position:absolute;left:185px;top:0;height:34px;padding:0 26px;background:var(--ink);font-size:17px;display:flex;align-items:center;clip-path:polygon(0 0,100% 0,93% 100%,4% 100%)}
.quote{position:absolute;left:200px;top:44px;width:800px;text-align:center;font-size:17px;line-height:1.3}
.quote .by{font-weight:700;display:block}

/* coaches */
.coaches{left:0;top:2240px;width:1200px;height:433px;background:#f4f4fa}
.coach{position:absolute;top:30px;width:300px;text-align:center}
.portrait{width:160px;height:160px;margin:0 auto 18px;border-radius:14px;background:linear-gradient(160deg,#9aa4b5,#4d5566);box-shadow:0 3px 8px rgba(0,0,0,.35);border:4px solid var(--white)}
.coach h5{font-size:17px;font-weight:500}
.coach .mail{font-size:16px;margin-bottom:30px}
.coach p{font-size:16px;line-height:1.3;width:240px;margin:0 auto}
.divider{position:absolute;left:581px;top:70px;width:1px;height:300px;background:#c9c9d6}

/* footer */
.footer{left:0;top:2673px;width:1200px;height:242px;background:var(--footer);color:#e6e6e6;font-size:16px}
.footer .tab{background:var(--red);color:var(--white);font-weight:500;left:197px;padding:0 44px}
.contact{position:absolute;left:213px;top:60px;line-height:1.35}
.contact .gap{margin-top:24px}
.follow{position:absolute;left:729px;top:42px;display:flex;align-items:center;gap:16px}
.social{width:44px;height:44px;border-radius:50%;background:#8d8d8d;border:3px solid #bdbdbd}
.copyright{position:absolute;left:717px;top:185px}
</style>
</head>
<body>

<header class="topbar abs">
  <div class="brand abs">
    <span class="brand-mark"></span>
    <div><div class="brand-name">HARBE KRONA</div><div class="brand-sub">LIVSSTILSCOACHING</div></div>
  </div>
</header>

<section class="hero abs" role="img" aria-label="Blue world map backdrop behind a photo of the two coaches standing together"></section>
<div class="hero-people abs" role="img" aria-label="Portrait photo of the two coaches"></div>
<div class="hero-tagline abs">Livsstilscoaching Lorem ipsum dolor sit amet, consectetuer adipiscing elit.</div>

<article class="welcome abs">
  <h1><span class="dot"></span>WELCOME TO TRIVSELSNYCKELN</h1>
  <p>Livsstilscoaching Lorem ipsum dolor sit amet, consectetuer adipiscing elit. Aenean commodo ligula eget dolor. Aenean massa. Cum sociis natoque penatibus et magnis dis parturient montes, nascetur ridiculus mus. Donec quam felis, ultricies nec, pellentesque eu, pretium quis, sem. Nulla consequat massa quis enim.</p>
  <p>Donec pede justo, fringilla vel, aliquet nec, vulputate eget, arcu. In enim justo, rhoncus ut, imperdiet a, venenatis vitae, justo. Nullam dictum felis eu pede mollis pretium. Integer tincidunt. Cras dapibus. Vivamus elementum semper nisi. Aenean vulputate eleifend tellus. Aenean leo ligula, porttitor eu, consequat vitae, eleifend ac, enim. <span class="read-more">read more</span> <svg class="chev" width="18" height="16" viewBox="0 0 18 16"><path d="M1 1l7 7-7 7M9 1l7 7-7 7" fill="none" stroke="var(--orange)" stroke-width="3"/></svg></p>
</article>

<section class="reasons abs">
  <h2 class="section-title"><svg width="18" height="18" viewBox="0 0 18 18"><path d="M2 1l12 8-12 8z" fill="#4fa3e0"/></svg>REASONS WHY CHOOSE COACHING</h2>
  <div class="reason" style="left:185px"><svg width="58" height="76" viewBox="0 0 58 76"><path d="M29 74C29 74 3 42 3 27a26 26 0 0 1 52 0c0 15-26 47-26 47z" fill="#fff"/><circle cx="29" cy="27" r="17" fill="var(--red)"/><text x="29" y="36" text-anchor="middle" font-size="24" font-style="italic" fill="#fff" font-family="Noto Sans,sans-serif">1</text></svg><strong>Livsstilscoaching</strong>Lorem ipsum dolor sit amet, consectetuer adipiscing elit.<span class="curl"></span></div>
  <div class="reason" style="left:398px"><svg width="58" height="76" viewBox="0 0 58 76"><path d="M29 74C29 74 3 42 3 27a26 26 0 0 1 52 0c0 15-26 47-26 47z" fill="#fff"/><circle cx="29" cy="27" r="17" fill="var(--red)"/><text x="29" y="36" text-anchor="middle" font-size="24" font-style="italic" fill="#fff" font-family="Noto Sans,sans-serif">2</text></svg><strong>Livsstilscoaching</strong>Lorem ipsum dolor sit amet, consectetuer adipiscing elit.<span class="curl"></span></div>
  <div class="reason" style="left:613px"><svg width="58" height="76" viewBox="0 0 58 76"><path d="M29 74C29 74 3 42 3 27a26 26 0 0 1 52 0c0 15-26 47-26 47z" fill="#fff"/><circle cx="29" cy="27" r="17" fill="var(--red)"/><text x="29" y="36" text-anchor="middle" font-size="24" font-style="italic" fill="#fff" font-family="Noto Sans,sans-serif">3</text></svg><strong>Livsstilscoaching</strong>Lorem ipsum dolor sit amet, consectetuer adipiscing elit.<span class="curl"></span></div>
  <div class="reason" style="left:825px"><svg width="58" height="76" viewBox="0 0 58 76"><path d="M29 74C29 74 3 42 3 27a26 26 0 0 1 52 0c0 15-26 47-26 47z" fill="#fff"/><circle cx="29" cy="27" r="17" fill="var(--red)"/><text x="29" y="36" text-anchor="middle" font-size="24" font-style="italic" fill="#fff" font-family="Noto Sans,sans-serif">4</text></svg><strong>Livsstilscoaching</strong>Lorem ipsum dolor sit amet, consectetuer adipiscing elit.<span class="curl"></span></div>
</section>

<section class="sessions abs">
  <h2 class="section-title"><svg width="22" height="16" viewBox="0 0 22 16"><path d="M1 1l7 7-7 7M10 1l7 7-7 7" fill="none" stroke="var(--orange)" stroke-width="3"/></svg>OUR TYPICAL COACHING SESSIONS:</h2>
  <div class="body">
    <p>Lorem ipsum dolor sit amet, consectetuer adipiscing elit. Aenean commodo ligula eget dolor. Aenean massa. Cum sociis natoque penatibus et magnis dis parturient montes, nascetur ridiculus mus. Donec quam felis, ultricies nec, pellentesque eu, pretium quis, sem. Nulla consequat massa quis enim.</p>
    <ul class="bullets">
      <li><span class="dot"></span>Lorem ipsum dolor sit amet, consectetuer adipiscing elit.</li>
      <li><span class="dot"></span>Lorem ipsum dolor sit amet, consectetuer adipiscing elit.</li>
      <li><span class="dot"></span>Lorem ipsum dolor sit amet, consectetuer adipiscing elit.</li>
      <li><span class="dot"></span>Lorem ipsum dolor sit amet, consectetuer adipiscing elit.</li>
    </ul>
    <h3>DONEC PEDE JUSTO, FRINGILLA VEL?</h3>
    <p class="para">aliquet nec, vulputate eget, arcu. In enim justo, rhoncus ut, imperdiet a, venenatis vitae, justo. Nullam dictum felis eu pede mollis pretium. Integer tincidunt. Cras dapibus. Vivamus</p>
    <h3>DONEC PEDE JUSTO, FRINGILLA VEL?</h3>
    <p class="para">aliquet nec, vulputate eget, arcu. In enim justo, rhoncus ut, imperdiet a, venenatis vitae, justo. Nullam dictum felis eu pede mollis pretium. Integer tincidunt. Cras dapibus. Vivamus</p>
  </div>
</section>

<section class="services abs">
  <h2 class="section-title"><svg width="22" height="16" viewBox="0 0 22 16"><path d="M1 1l7 7-7 7M10 1l7 7-7 7" fill="none" stroke="var(--orange)" stroke-width="3"/></svg>OUR SERVICES:</h2>
  <div class="plans">
    <div class="plan"><div class="medal bronze" role="img" aria-label="Bronze medal graphic"></div><h4>BRONZE</h4><div class="kind">(SINGLE COACHING SESSION)</div><div class="note">aliquet nec, vulputate eget, arcu.</div><div class="order"><span class="circle"></span>CLICK ORDER</div></div>
    <div class="plan"><div class="medal silver" role="img" aria-label="Silver medal graphic"></div><h4>SILVER</h4><div class="kind">(SMALL-PACKAGE)</div><div class="note">aliquet nec, vulputate eget, arcu.</div><div class="order"><span class="circle"></span>CLICK ORDER</div></div>
    <div class="plan"><div class="medal gold" role="img" aria-label="Gold medal graphic"></div><h4>GOLD</h4><div class="kind">(LARGE-PACKAGE)</div><div class="note">aliquet nec, vulputate eget, arcu.</div><div class="order"><span class="circle"></span>CLICK ORDER</div></div>
  </div>
  <p class="guarantee">Money- Back Guarantee: If you are not satisfied , please contact us within 14 days after the first coaching call, so you get the money back .</p>
</section>

<section class="testimonials abs">
  <div class="tab">TESTIMONIALS</div>
  <blockquote class="quote">Uppiggande och inspirerande! Kommer med enkla vardagstips såväl som svårare tips. Ett roligt sätt att få en spark i baken, så att ekonomi-energin bibehålls! Tack för ett bra samtal!" <span class="by">- JOSEFIN BRANDEBY</span></blockquote>
</section>

<section class="coaches abs">
  <div class="coach" style="left:191px"><div class="portrait" role="img" aria-label="Portrait photo of coach Torbjörn Falkdal"></div><h5>TORBJÖRN FALKDAL</h5><div class="mail">torbjorn@harbekrona.se</div><p>Lorem ipsum dolor sit amet, consectetuer adipiscing elit. Aenean commodo ligula eget dolor. Aenean massa. Cum sociis natoque penatibus et</p></div>
  <div class="divider"></div>
  <div class="coach" style="left:670px"><div class="portrait" role="img" aria-label="Portrait photo of coach Henrik Lövgren"></div><h5>HENRIK LÖVGREN</h5><div class="mail">henrik@harbekrona.se</div><p>Lorem ipsum dolor sit amet, consectetuer adipiscing elit. Aenean commodo ligula eget dolor. Aenean massa. Cum sociis natoque penatibus et</p></div>
</section>

<footer class="footer abs">
  <div class="tab">REACH US AT:</div>
  <address class="contact" style="font-style:normal">
    Contact Us:
    <div class="gap">Harbe Krona AB<br>Ekbackevägen 12<br>412 60 Göteborg</div>
    <div class="gap">Vid frågor kontakta oss på team@harbekrona.se</div>
  </address>
  <div class="follow">Follow us on: <span class="social" style="margin-left:12px"></span><span class="social"></span></div>
  <div class="copyright">Copyright 2016 Harbe Krona AB</div>
</footer>

</body>
</html>
```